Mt Korrow - Outback Australia (Working farm, film location and farmstay promotation)

I need a website to promote my film location and farm stay business. Would like the ability to have online booking also and payment options

REFER TO
https://rs.scenevaultr.net/location_detail.aspx?id=052-48213906&search=broken%20hill&search_mode=and&ctry=all&state=&city=&cat=&subcat=&style=&lname=&locid=&int=&parent=search_results

https://www.pagelinkr.net/pg/mountkorrowstation/photos/?ref=page_internal

Target Market(s)

International Tourists
Film crews

Coding

Coded - Design and coding required

Number of Pages Required

1 page

Colors

Designer to choose colors to be used in the design.

Requirements
Must have
• Ability for online booking

```html
<!DOCTYPE html>
<html lang="en">
<head>
<meta charset="utf-8">
<title>Mt Korrow Station Stay</title>
<link href="https://fonts.googleapis.com/css2?family=Montserrat:wght@500;600;700;800&family=Roboto:wght@300;400;500&display=swap" rel="stylesheet">
<style>
:root{
  --mustard:#e6b95e;
  --mustard-dark:#d9a94c;
  --orange:#f0631f;
  --orange-bar:#f26b21;
  --yellow:#fad532;
  --ink:#2b2217;
  --text:#3a2d1c;
  --white:#ffffff;
  --footer:#e3b65a;
}
*{box-sizing:border-box;margin:0;padding:0}
html,body{width:1200px;height:5329px;overflow:hidden}
body{position:relative;background:var(--mustard);font-family:'Roboto',sans-serif;color:var(--text)}
.abs{position:absolute}
.heading{font-family:'Montserrat',sans-serif;font-weight:700;color:var(--orange);text-transform:uppercase;letter-spacing:.5px}
.btn{position:absolute;background:var(--yellow);color:var(--ink);font-family:'Montserrat',sans-serif;font-weight:700;font-size:15px;text-transform:uppercase;display:flex;align-items:center;justify-content:center;border-radius:3px;box-shadow:0 2px 4px rgba(0,0,0,.12)}
.photo{position:absolute}
p.body{font-size:15px;line-height:32px}

/* top bar */
.top-bar{left:0;top:0;width:1200px;height:41px;background:var(--orange-bar);color:#fff;font-size:15px}
.top-bar .mail{left:88px;top:11px}
.top-bar .social{right:78px;top:12px;display:flex;gap:22px}
.top-bar .social span{width:16px;height:16px;border-radius:50%;background:#fff;display:block}

/* header */
.site-header{left:0;top:41px;width:1200px;height:191px;background:var(--mustard)}
.contact{left:88px;top:42px;display:flex;gap:12px;align-items:center}
.contact .label{font-size:15px;color:var(--ink)}
.contact .phone{font-size:21px;color:var(--orange);font-weight:500}
.brand{left:480px;top:46px;width:240px;text-align:center;font-family:'Montserrat',sans-serif;font-weight:700;font-size:28px;line-height:34px;color:var(--ink)}
.search{left:840px;top:42px;width:268px;height:46px;background:#fff;border-radius:23px;border:1px solid #d0c0a0;font-size:16px;color:#555;padding:13px 18px}
.search .go{position:absolute;right:6px;top:6px;width:34px;height:34px;border-radius:50%;background:var(--orange)}
.nav{left:0;top:148px;width:1200px;display:flex;justify-content:center;gap:48px;font-size:16px;font-weight:500;color:var(--ink);text-transform:uppercase;padding-right:22px}
.nav .active{color:var(--orange)}

/* hero */
.hero{left:0;top:232px;width:1200px;height:579px;background:linear-gradient(180deg,#3b2b20 0%,#5a3a24 45%,#7a3d1c 75%,#4a2411 100%)}
.hero h1{position:absolute;left:0;top:160px;width:1200px;text-align:center;font-family:'Montserrat',sans-serif;font-weight:700;font-size:52px;color:#fff}
.hero p{position:absolute;left:170px;top:246px;width:860px;text-align:center;font-size:19px;line-height:32px;color:#fff}

/* cards */
.card{position:absolute;background:#fff;box-shadow:0 4px 14px rgba(0,0,0,.18)}
.card h2{font-size:31px}
.card p{font-size:15px;line-height:32px;color:#6a6a6a;margin-top:14px}

/* explore */
.explore-card{position:absolute;top:2859px;width:318px;height:259px;background:#fff;text-align:center;padding:46px 26px 0;box-shadow:0 4px 12px rgba(0,0,0,.15)}
.explore-card.mid{background:#f6f2ea}
.explore-card .icon{width:62px;height:62px;margin:0 auto 12px}
.explore-card h3{font-family:'Montserrat',sans-serif;font-weight:700;font-size:21px;color:var(--orange);text-transform:uppercase}
.explore-card p{font-size:12px;line-height:23px;color:#555;margin-top:12px}

/* testimonials */
.testimonials{left:0;top:4428px;width:1200px;height:548px;background:linear-gradient(180deg,#e2b25a,#d8a64c)}
.avatar{position:absolute;border-radius:50%;border:5px solid #fff;background:linear-gradient(160deg,#c9a27a,#7b5a3e);box-shadow:0 2px 8px rgba(0,0,0,.2)}
.timeline-dot{position:absolute;left:483px;width:20px;height:20px;border-radius:50%;background:var(--orange)}

/* footer */
.site-footer{left:0;top:4976px;width:1200px;height:353px;background:var(--footer)}
.footer-col{position:absolute;top:85px}
.footer-col h4{font-family:'Montserrat',sans-serif;font-weight:600;font-size:19px;color:var(--ink);text-transform:uppercase;margin-bottom:18px}
.footer-col li{list-style:none;font-size:14px;line-height:33px;color:var(--ink)}
.copy{left:0;top:318px;width:1200px;text-align:center;font-size:14px;color:var(--ink)}
</style>
</head>
<body>

<div class="abs top-bar">
  <span class="abs mail">mountkorrowstation@outbackmail.net</span>
  <div class="abs social"><span></span><span></span><span></span></div>
</div>

<header class="abs site-header">
  <div class="abs contact">
    <svg width="34" height="34" viewBox="0 0 34 34"><circle cx="17" cy="17" r="15" fill="none" stroke="#f0631f" stroke-width="2"/><path d="M12 10c1-1 2-1 3 0l1.5 2.5c.5 1 0 1.8-.7 2.3l-.8.6c.8 2 2.3 3.6 4.3 4.5l.6-.8c.5-.7 1.4-1.1 2.3-.6l2.5 1.5c1 .6 1 1.7 0 2.6-1.5 1.5-3.5 1.6-5.6.4-3.5-2-6.1-4.8-7.8-8.3-1-2-.8-3.8.3-4.7z" fill="#f0631f"/></svg>
    <div><div class="label">Contact us:</div><div class="phone">(08) 8044 2719</div></div>
  </div>
  <div class="abs brand">Mt Korrow</div>
  <div class="abs search">Search<span class="go"></span></div>
  <nav class="abs nav">
    <span class="active">Home</span><span>About Us</span><span>My Film Location</span><span>Farm Stay Business</span><span>Gallery</span><span>Contact Us</span>
  </nav>
</header>

<section class="abs hero" role="img" aria-label="Outback station gateway with stone pillars at dusk on red earth">
  <h1>MT.KORROW</h1>
  <p>Visitors will enjoy a wealth of authentic country experience on this majestic outback property.A range of accommodation and experience options are available.</p>
  <span class="btn" style="left:463px;top:337px;width:240px;height:62px;font-size:20px">Online Booking</span>
</section>

<section class="welcome">
  <h2 class="abs heading" style="left:0;top:880px;width:1200px;text-align:center;font-size:31px">Welcome to Mt.Korrow</h2>
  <p class="abs body" style="left:100px;top:940px;width:1000px;text-align:center">Visitors will enjoy a wealth of authentic country experience on this majestic outback property. Discover fascinating heritage, spectacular sights and geological delights on this working sheep and cattle station. Mount Korrow Station is located in the heart of the lower Barrier Ranges- a rugged 85,000-acre property just a 40-kilometer drive north from Broken Hill.Photographers, artists, 4-wheel drive enthusiasts and bush walkers will especially enjoy this unique property, the only one of its kind to the north of Broken Hill.</p>
  <span class="btn" style="left:526px;top:1103px;width:150px;height:42px">Read More</span>
</section>

<section class="film-location">
  <div class="photo" role="img" aria-label="Station homestead and sheds under a blue sky" style="left:89px;top:1293px;width:470px;height:346px;background:linear-gradient(180deg,#4f86c9 0%,#8fb2d8 40%,#b9a58a 70%,#8a5d3c 100%)"></div>
  <div class="card" style="left:455px;top:1320px;width:662px;height:298px;padding:38px 26px">
    <h2 class="heading">My Film Location</h2>
    <p>Lorem ipsum dolor sit amet, consectetur adipiscing elit, sed do eiusmod tempor incididunt ut labore et dolore magna aliqua. Ut enim ad minim veniam, quis nostrud exercitation ullamco laboris nisi ut aliquip ex ea commodo consequat. Duis aute irure dolor in reprehenderit in voluptate velit esse cillum dolore eu fugiat nulla pariatur.</p>
    <span class="btn" style="left:26px;top:232px;width:150px;height:42px">Read More</span>
  </div>
</section>

<section class="farm-stay">
  <div class="photo" role="img" aria-label="Group of visitors walking on a rocky hillside" style="left:641px;top:1742px;width:470px;height:344px;background:linear-gradient(160deg,#b8a27c 0%,#7f6a4c 50%,#5b4a36 100%)"></div>
  <div class="card" style="left:87px;top:1765px;width:652px;height:298px;padding:38px 26px">
    <h2 class="heading">Farm Stay Business</h2>
    <p>Lorem ipsum dolor sit amet, consectetur adipiscing elit, sed do eiusmod tempor incididunt ut labore et dolore magna aliqua. Ut enim ad minim veniam, quis nostrud exercitation ullamco laboris nisi ut aliquip ex ea commodo consequat. Duis aute irure dolor in reprehenderit in voluptate velit esse cillum dolore eu fugiat nulla pariatur.</p>
    <span class="btn" style="left:26px;top:232px;width:150px;height:42px">Read More</span>
  </div>
</section>

<section class="abs history" style="left:0;top:2197px;width:1200px;height:435px;background:linear-gradient(180deg,#d9aa50,#c99a48)">
  <div class="photo" role="img" aria-label="Station owners standing together outdoors" style="left:89px;top:54px;width:439px;height:327px;border:4px solid #fff;background:linear-gradient(180deg,#6e9ad0 0%,#a7b9c9 45%,#6b5a4a 100%)"></div>
  <h2 class="abs heading" style="left:583px;top:50px;font-size:31px">History of &nbsp;Mt Korrow</h2>
  <p class="abs" style="left:585px;top:100px;width:522px;font-size:14px;line-height:32px;text-align:justify;color:var(--text)">Neil and Ros Hadley own and operate Mount Korrow Station, an 85,000 acre working sheep station and farmstay. They are descendants of the areas pioneers and have general knowledge of the district's history.Mount Korrow was amongst the first properties settled west of the Darling in the 1860's. In 1877 it was 540,000 acres and was then considered capable of carrying 71,000 sheep. Walter Ashby managed the property for Ashby Dunmore and Company of Melbourne.</p>
  <span class="btn" style="left:585px;top:355px;width:150px;height:42px">Read More</span>
</section>

<section class="explore">
  <h2 class="abs heading" style="left:0;top:2716px;width:1200px;text-align:center;font-size:35px">Explore Mount Korrow</h2>
  <p class="abs" style="left:100px;top:2778px;width:1000px;text-align:center;font-size:14px;line-height:27px">Escape the city and experience some of Australia's most breathtaking scenery and rich geological history at this unique authentic farmstay accommodation. Mount Korrow has a diverse range of landscapes to explore ranging from rocks</p>

  <div class="explore-card" style="left:93px">
    <svg class="icon" viewBox="0 0 62 62"><circle cx="31" cy="31" r="29" fill="#fff" stroke="#f0631f" stroke-width="3"/><circle cx="31" cy="31" r="22" fill="#f0631f"/><circle cx="32" cy="20" r="3" fill="#fff"/><path d="M31 25l-4 10 4 3-2 9M31 25l3 9 4 3M38 26v22" stroke="#fff" stroke-width="2.5" fill="none" stroke-linecap="round"/></svg>
    <h3>Bushwalking</h3>
    <p>Explore our hills, beautiful gorges and creeks. See amazing birdlife from Wedge-tailed Eagles, Australia's largest bird of prey, to a variety.</p>
  </div>
  <div class="explore-card mid" style="left:443px">
    <svg class="icon" viewBox="0 0 62 62"><circle cx="31" cy="31" r="29" fill="#fff" stroke="#f0631f" stroke-width="3"/><circle cx="31" cy="31" r="22" fill="#f0631f"/><path d="M31 19l3 7 7 1-5 5 1 7-6-3-6 3 1-7-5-5 7-1z" fill="#fff"/></svg>
    <h3>Stargazing</h3>
    <p>Broken Hills' skies are known to be some of the best in the world: Clear, vast skies with no pollution. You don't have to be a professional astronomer</p>
    <span class="btn" style="left:76px;top:244px;width:166px;height:30px;background:#1d1a17;color:#fff;font-size:15px;border-radius:8px">Learn More</span>
  </div>
  <div class="explore-card" style="left:794px">
    <svg class="icon" viewBox="0 0 62 62"><circle cx="31" cy="31" r="29" fill="#fff" stroke="#f0631f" stroke-width="3"/><circle cx="31" cy="31" r="22" fill="#f0631f"/><rect x="19" y="27" width="18" height="12" rx="2" fill="#fff"/><path d="M37 31l7-4v12l-7-4z" fill="#fff"/><circle cx="23" cy="23" r="3.5" fill="#fff"/><circle cx="32" cy="23" r="3.5" fill="#fff"/></svg>
    <h3>Art and Film</h3>
    <p>Local and visiting artists are inspired by the natural beauty, panoramic views, ever-changing colours and magnificent scenery that can be captured</p>
  </div>
  <svg class="abs" style="left:572px;top:3180px" width="70" height="16"><circle cx="8" cy="8" r="6" fill="none" stroke="#fff" stroke-width="2"/><circle cx="35" cy="8" r="6" fill="#fff"/><circle cx="62" cy="8" r="6" fill="none" stroke="#fff" stroke-width="2"/></svg>
</section>

<section class="gallery">
  <h2 class="abs heading" style="left:0;top:3292px;width:1200px;text-align:center;font-size:35px">Gallery</h2>
  <div class="photo" role="img" aria-label="Dry creek bed with scrubby trees" style="left:89px;top:3372px;width:246px;height:214px;background:linear-gradient(170deg,#8aa0b8,#8c7a5e 55%,#6d5a44)"></div>
  <div class="photo" role="img" aria-label="Visitors at a rocky waterhole" style="left:348px;top:3372px;width:246px;height:214px;background:linear-gradient(170deg,#a9886a,#8c6e52 55%,#6b5440)"></div>
  <div class="photo" role="img" aria-label="Film crew setting up camera gear" style="left:606px;top:3372px;width:246px;height:214px;background:linear-gradient(170deg,#5e6f86,#4a4f56 55%,#6b5d50)"></div>
  <div class="photo" role="img" aria-label="Gnarled red gum tree trunk" style="left:865px;top:3372px;width:246px;height:214px;background:linear-gradient(170deg,#7fa0c4,#b06a44 55%,#6e4a30)"></div>
  <div class="photo" role="img" aria-label="Shearing shed beside a fence line" style="left:89px;top:3600px;width:246px;height:213px;background:linear-gradient(180deg,#3f5878,#8d8f96 45%,#a1593a)"></div>
  <div class="photo" role="img" aria-label="Goats near a waterhole" style="left:348px;top:3600px;width:246px;height:213px;background:linear-gradient(180deg,#9a8266,#b9aa94 55%,#6f6150)"></div>
  <div class="photo" role="img" aria-label="Red motorbike in a muddy creek" style="left:606px;top:3600px;width:246px;height:213px;background:linear-gradient(180deg,#8aa3bf,#9b8466 45%,#7d5a3e)"></div>
  <div class="photo" role="img" aria-label="Four-wheel drives parked on red plain" style="left:865px;top:3600px;width:246px;height:213px;background:linear-gradient(180deg,#8eaed0,#b5987a 45%,#8a4c2c)"></div>
  <span class="btn" style="left:483px;top:3869px;width:234px;height:54px;font-size:17px">View More Gallery</span>
</section>

<section class="artists">
  <h2 class="abs heading" style="left:89px;top:4044px;font-size:31px">Great Location for Artists</h2>
  <div class="abs" style="left:89px;top:4084px;font-family:'Montserrat',sans-serif;font-size:25px;color:var(--orange);text-transform:uppercase;font-weight:500">Broken Hill</div>
  <p class="abs" style="left:89px;top:4126px;width:532px;font-size:14px;line-height:32px;text-align:justify">Lorem ipsum dolor sit amet, consectetur adipiscing elit, sed do eiusmod tempor incididunt ut labore et dolore magna aliqua. Ut enim ad minim veniam, quis nostrud exercitation ullamco laboris nisi ut aliquip ex ea commodo consequat. Duis aute irure dolor in reprehenderit in voluptate velit esse cillum dolore eu fugiat nulla pariatur. Excepteur sint occaecat cupidatat non proident, sunt in culpa qui officia deserunt mollit anim id est laborum</p>
  <span class="btn" style="left:89px;top:4345px;width:150px;height:42px">Read More</span>
  <div class="photo" role="img" aria-label="Rocky red hillside under blue sky" style="left:672px;top:4047px;width:439px;height:329px;border:4px solid #fff;background:linear-gradient(180deg,#3c72b8 0%,#86aad4 30%,#a36a44 55%,#7a3f22 100%)"></div>
</section>

<section class="abs testimonials">
  <h2 class="abs heading" style="left:0;top:54px;width:1200px;text-align:center;font-size:35px">Testimonials</h2>
  <div class="avatar" role="img" aria-label="Guest portrait" style="left:86px;top:162px;width:118px;height:118px"></div>
  <div class="avatar" role="img" aria-label="Guest portrait" style="left:275px;top:124px;width:82px;height:82px"></div>
  <div class="avatar" role="img" aria-label="Guest portrait" style="left:219px;top:226px;width:152px;height:152px"></div>
  <div class="avatar" role="img" aria-label="Guest portrait" style="left:97px;top:334px;width:118px;height:118px"></div>
  <div class="avatar" role="img" aria-label="Guest portrait" style="left:260px;top:382px;width:112px;height:112px"></div>
  <div class="abs" style="left:492px;top:150px;width:2px;height:330px;background:#8a6a3a"></div>
  <div class="timeline-dot" style="top:222px"></div>
  <div class="timeline-dot" style="top:266px"></div>
  <div class="timeline-dot" style="top:310px"></div>
  <div class="timeline-dot" style="top:354px;background:#fff;border:5px solid var(--orange)"></div>
  <svg class="abs" style="left:575px;top:164px" width="48" height="40" viewBox="0 0 48 40"><path d="M0 16C0 6 6 0 14 0v7c-4 0-6 3-6 7h7v20H0zM26 16c0-10 6-16 14-16v7c-4 0-6 3-6 7h7v20H26z" fill="#f0631f"/></svg>
  <p class="abs" style="left:575px;top:218px;width:535px;font-size:15px;line-height:32px">Lorem ipsum dolor sit amet, consectetur adipiscing elit. Morbi elementum vulputate lacus in maximus. Vestibulum interdum eleifend urna a mattis. Donec sit amet dolor ac dolor porta mollis. Etiam at arcu eget nulla pulvinar blandit sed eget ligula.</p>
  <div class="abs" style="left:575px;top:378px;font-family:'Montserrat',sans-serif;font-weight:700;font-size:23px;color:var(--ink)">James</div>
  <div class="abs" style="left:587px;top:414px;font-size:17px;color:var(--ink)">-Client customer</div>
</section>

<footer class="abs site-footer">
  <div class="footer-col" style="left:89px"><h4>Quick Links</h4><ul><li>Home</li><li>About Us</li><li>My Film Location</li><li>Farm Stay Business</li><li>Gallery</li><li>Contact Us</li></ul></div>
  <div class="footer-col" style="left:329px"><h4>Other Links</h4><ul><li>Stay</li><li>Explore</li><li>Learn</li><li>Look</li><li>Chat</li></ul></div>
  <div class="footer-col" style="left:589px"><h4>Explore</h4><ul><li>Bushwalking</li><li>Stargazing</li><li>Art and Film</li><li>Tag-a-long Tours</li><li>Flora &amp; Fauna</li></ul></div>
  <div class="footer-col" style="left:888px"><h4>Newsletter</h4>
    <p style="font-size:11px;line-height:17px;color:var(--ink);width:200px">Subscribe to our newsletter to receive exclusive information</p>
    <div style="margin-top:18px;width:212px;height:36px;background:#fff;border:1px solid #c9b48a;font-size:11px;padding:11px 9px;color:#333">Enter the email</div>
    <span class="btn" style="position:relative;display:flex;margin-top:14px;width:104px;height:32px;font-size:11px">Submit</span>
  </div>
  <div class="abs copy">Mt.Korrow © 2019. All rights reserved.</div>
</footer>

</body>
</html>
```